KTLR Unique Letterhead for Financial Services Business

I am looking for a letterhead design to match our branding colours. I do not want to see anything generic that could be created in word, I can do that myself, I am after something with a bit of designer flair. Once completed I will need files in a print ready format (including bleed area).

I have included our logo file and also our new business card design but get creative.

Industry/Entity Type

Financial Services

Font styles to use
Other font styles liked:
• raleway

Colors
00AB8E
00BBA5
67D7C9
C6EFE9
E9F9F6

Requirements
Must have
• Must be consisten with logo branding colours.
Should not have
• Anything generic that I could create myself in word

```html
<!DOCTYPE html>
<html lang="en">
<head>
<meta charset="utf-8">
<title>KTLR Financial Services – Letterhead</title>
<link rel="stylesheet" href="https://fonts.googleapis.com/css2?family=Raleway:wght@400;500&family=Source+Sans+3:wght@400;500&display=swap">
<style>
  :root {
    --stage: #8c8c8c;
    --paper: #ffffff;
    --teal: #0e9a92;
    --teal-deep: #00857d;
    --slate: #8a8a8a;
    --ink: #1f2a44;
    --navy: #1d3f6b;
    --mist: #ececec;
    --mist-soft: #f6f6f6;
    --rule: #9a9a9a;
  }
  * { margin: 0; padding: 0; box-sizing: border-box; }
  html, body { width: 1200px; height: 900px; overflow: hidden; }
  body { background: var(--stage); position: relative; }

  .letterhead {
    position: absolute;
    top: 87px;
    width: 442px;
    height: 626px;
    background: var(--paper);
    overflow: hidden;
  }
  .letterhead--primary { left: 131px; }
  .letterhead--alternate { left: 627px; }

  .monogram-decor {
    position: absolute;
    background: linear-gradient(160deg, var(--mist) 0%, var(--mist-soft) 100%);
    border-radius: 0 90px 90px 0;
  }
  .letterhead--primary .monogram-decor { left: 39px; top: 198px; width: 375px; height: 323px; }
  .letterhead--alternate .monogram-decor { left: 0; top: 358px; width: 196px; height: 268px; }

  .brand {
    position: absolute;
    left: 78px;
    top: 88px;
    width: 142px;
    text-align: center;
  }
  .brand__name {
    font-family: "Raleway", sans-serif;
    font-weight: 500;
    font-size: 30px;
    letter-spacing: 3px;
    color: var(--teal);
    line-height: 1;
  }
  .brand__tagline {
    margin-top: 3px;
    font-family: "Raleway", sans-serif;
    font-weight: 400;
    font-size: 8px;
    letter-spacing: 1.6px;
    color: var(--teal);
  }

  .contact {
    position: absolute;
    left: 283px;
    top: 72px;
    list-style: none;
    font-family: "Raleway", sans-serif;
    font-size: 10.5px;
    color: var(--ink);
  }
  .contact__item { display: flex; align-items: center; height: 14.5px; gap: 6px; }
  .contact__icon { width: 10px; height: 10px; flex: none; }

  .edge-tab {
    position: absolute;
    right: 0;
    top: 66px;
    width: 18px;
    height: 38px;
    background: var(--teal);
  }

  .sender {
    position: absolute;
    left: 77px;
    top: 161px;
    font-family: "Source Sans 3", sans-serif;
    font-weight: 500;
    font-size: 11.5px;
    line-height: 16px;
    color: var(--navy);
  }

  .body-copy {
    position: absolute;
    left: 77px;
    top: 213px;
    width: 294px;
    font-family: "Source Sans 3", sans-serif;
    font-size: 8px;
    line-height: 15.6px;
    color: var(--ink);
  }
  .body-copy p + p { margin-top: 15.6px; }

  .signature {
    position: absolute;
    left: 66px;
    top: 443px;
    width: 146px;
    height: 28px;
  }

  .address {
    position: absolute;
    left: 0;
    width: 100%;
    top: 580px;
    text-align: center;
    font-family: "Raleway", sans-serif;
    font-size: 10.5px;
    color: var(--ink);
  }

  .footer-band {
    position: absolute;
    left: 0;
    bottom: 0;
    width: 442px;
    height: 20px;
  }
</style>
</head>
<body>

  <article class="letterhead letterhead--primary">
    <div class="monogram-decor" role="img" aria-label="Large faint brand monogram watermark"></div>
    <div class="edge-tab"></div>
    <header class="brand">
      <div class="brand__name">KTLR</div>
      <div class="brand__tagline">Financial Services</div>
    </header>
    <ul class="contact">
      <li class="contact__item">
        <svg class="contact__icon" viewBox="0 0 10 10"><circle cx="5" cy="5" r="4.4" fill="none" stroke="var(--teal)" stroke-width="1"/><path d="M3.6 2.8l1 1-.6.7a3 3 0 0 0 1.5 1.5l.7-.6 1 1-.7.8C4.8 7 3 5.2 2.8 3.5z" fill="var(--teal)"/></svg>
        <span>555 0199 204</span>
      </li>
      <li class="contact__item">
        <svg class="contact__icon" viewBox="0 0 10 10"><circle cx="5" cy="5" r="5" fill="var(--teal)"/><rect x="2.6" y="3.4" width="4.8" height="3.2" fill="none" stroke="#fff" stroke-width=".7"/><path d="M2.6 3.4L5 5.3l2.4-1.9" fill="none" stroke="#fff" stroke-width=".7"/></svg>
        <span>hello@ktlrmail.com</span>
      </li>
      <li class="contact__item">
        <svg class="contact__icon" viewBox="0 0 10 10"><circle cx="5" cy="5" r="5" fill="var(--teal)"/><circle cx="5" cy="5" r="2.4" fill="none" stroke="#fff" stroke-width=".7"/><path d="M2.6 5h4.8M5 2.6v4.8" stroke="#fff" stroke-width=".5"/></svg>
        <span>www.ktlrfinance.com</span>
      </li>
    </ul>
    <div class="sender">Mara Ellison<br>Manager</div>
    <div class="body-copy">
      <p>Lorem ipsum dolor sit amet, consectetuer adipiscing elit, sed diam nonummy nibh euismod tincidunt ut laoreet dolore magna aliquam erat volutpat. Ut wisi enim ad minim veniam, quis nostrud exerci tation ullamcorper suscipit lobortis nisl ut aliquip ex ea commodo consequat.</p>
      <p>Duis autem vel eum iriure dolor in hendrerit in vulputate velit esse molestie consequat, vel illum dolore eu feugiat nulla facilisis at vero zzril delenit augue duis dolore te feugait nulla facilisi.</p>
      <p>Lorem ipsum dolor sit amet, cons ectetuer adipiscing elit, sed diam nonummy nibh euismod tincidunt ut laoreet dolore magna aliquam erat volutpat. Ut wisi enim ad minim veniam, quis nostrud exerci tation ullamcorper suscipit lobortis nisl ut aliquip ex ea commodo consequat.</p>
    </div>
    <svg class="signature" viewBox="0 0 146 28">
      <rect x="0" y="4" width="146" height="18" fill="var(--mist)" role="img" aria-label="Handwritten signature"/>
      <line x1="4" y1="26" x2="146" y2="26" stroke="var(--rule)" stroke-width=".6"/>
    </svg>
    <div class="address">00 my address, lorem ipsum lane , lorem ipsum-2222</div>
    <svg class="footer-band" viewBox="0 0 442 20" preserveAspectRatio="none">
      <polygon points="0,0 220,0 208,20 0,20" fill="var(--teal)"/>
      <polygon points="226,0 442,0 442,20 214,20" fill="var(--slate)"/>
    </svg>
  </article>

  <article class="letterhead letterhead--alternate">
    <div class="monogram-decor" role="img" aria-label="Large faint brand monogram watermark"></div>
    <div class="edge-tab"></div>
    <header class="brand">
      <div class="brand__name">KTLR</div>
      <div class="brand__tagline">Financial Services</div>
    </header>
    <ul class="contact">
      <li class="contact__item">
        <svg class="contact__icon" viewBox="0 0 10 10"><circle cx="5" cy="5" r="4.4" fill="none" stroke="var(--teal)" stroke-width="1"/><path d="M3.6 2.8l1 1-.6.7a3 3 0 0 0 1.5 1.5l.7-.6 1 1-.7.8C4.8 7 3 5.2 2.8 3.5z" fill="var(--teal)"/></svg>
        <span>555 0199 204</span>
      </li>
      <li class="contact__item">
        <svg class="contact__icon" viewBox="0 0 10 10"><circle cx="5" cy="5" r="5" fill="var(--teal)"/><rect x="2.6" y="3.4" width="4.8" height="3.2" fill="none" stroke="#fff" stroke-width=".7"/><path d="M2.6 3.4L5 5.3l2.4-1.9" fill="none" stroke="#fff" stroke-width=".7"/></svg>
        <span>hello@ktlrmail.com</span>
      </li>
      <li class="contact__item">
        <svg class="contact__icon" viewBox="0 0 10 10"><circle cx="5" cy="5" r="5" fill="var(--teal)"/><circle cx="5" cy="5" r="2.4" fill="none" stroke="#fff" stroke-width=".7"/><path d="M2.6 5h4.8M5 2.6v4.8" stroke="#fff" stroke-width=".5"/></svg>
        <span>www.ktlrfinance.com</span>
      </li>
    </ul>
    <div class="sender">Mara Ellison<br>Manager</div>
    <div class="body-copy">
      <p>Lorem ipsum dolor sit amet, consectetuer adipiscing elit, sed diam nonummy nibh euismod tincidunt ut laoreet dolore magna aliquam erat volutpat. Ut wisi enim ad minim veniam, quis nostrud exerci tation ullamcorper suscipit lobortis nisl ut aliquip ex ea commodo consequat.</p>
      <p>Duis autem vel eum iriure dolor in hendrerit in vulputate velit esse molestie consequat, vel illum dolore eu feugiat nulla facilisis at vero zzril delenit augue duis dolore te feugait nulla facilisi.</p>
      <p>Lorem ipsum dolor sit amet, cons ectetuer adipiscing elit, sed diam nonummy nibh euismod tincidunt ut laoreet dolore magna aliquam erat volutpat. Ut wisi enim ad minim veniam, quis nostrud exerci tation ullamcorper suscipit lobortis nisl ut aliquip ex ea commodo consequat.</p>
    </div>
    <svg class="signature" viewBox="0 0 146 28">
      <rect x="0" y="4" width="146" height="18" fill="var(--mist)" role="img" aria-label="Handwritten signature"/>
      <line x1="4" y1="26" x2="146" y2="26" stroke="var(--rule)" stroke-width=".6"/>
    </svg>
    <div class="address">00 my address, lorem ipsum lane , lorem ipsum-2222</div>
    <svg class="footer-band" viewBox="0 0 442 20" preserveAspectRatio="none">
      <polygon points="0,0 220,0 208,20 0,20" fill="var(--teal)"/>
      <polygon points="226,0 442,0 442,20 214,20" fill="var(--slate)"/>
    </svg>
  </article>

</body>
</html>
```